Australian Solar Smart Home Provider needs business card design

We need a simple, clean, business card that shows who we are and gives the brand feeling. Please see the website (www.pelvora.com) and the attached logo as well. Please use this logo on the business card. As a business we do residential solar, batteries, smart home technology, and hot water solutions. We want the feeling to be accessible to ages 40-65 but at the same time be a bit on the technologically savvy side.
Also the primary purpose of the business card is to hand of and drive referrals - so we want everyone to have a referral code on the card and that aspect should stand out.
Things we want on the card with an example employee:
Name: Brent Malvaney
Position: Director of Sales and Marketing
telephone number office: 02 8736 2914
telephone number mobile: 0478 591 830
address: Suite 403, 19 Clover Lane, Sydney, NSW 2000
website: www.pelvora.com
Target Market(s)
Homeowners aged 35-60
Industry/Entity Type
Residential
Contact Information for Business Card
Name: Brent Malvaney
website: www.pelvora.com
referral code: Bmalvaney
Look and feel

```html
<!DOCTYPE html>
<html lang="en">
<head>
<meta charset="utf-8">
<title>Pelvora – Business Card</title>
<link href="https://fonts.googleapis.com/css2?family=Arimo:wght@400;700&display=swap" rel="stylesheet">
<style>
  :root {
    --page-bg: #e9e7e2;
    --card-bg: #ffffff;
    --ink-grey: #9a9a9a;
    --ink-soft: #b3b3b3;
    --brand-green: #7cc242;
    --brand-green-light: #a6d96a;
    --brand-green-dark: #5aa92c;
    --band-text: #ffffff;
  }
  html, body {
    margin: 0;
    padding: 0;
    width: 1200px;
    height: 885px;
    overflow: hidden;
    background: var(--page-bg);
    font-family: "Arimo", Arial, sans-serif;
  }
  .business-card {
    position: absolute;
    left: 360px;
    top: 52px;
    width: 480px;
    height: 780px;
    background: var(--card-bg);
    box-shadow: 0 6px 20px rgba(0,0,0,0.15);
    display: flex;
    flex-direction: column;
    align-items: center;
  }
  .brand {
    margin-top: 110px;
    display: flex;
    flex-direction: column;
    align-items: center;
  }
  .brand-mark {
    display: flex;
    align-items: center;
    gap: 14px;
  }
  .brand-dot {
    width: 34px;
    height: 34px;
    border-radius: 50%;
    background: var(--brand-green);
  }
  .brand-name {
    font-size: 64px;
    font-weight: 700;
    color: var(--ink-grey);
    letter-spacing: -1px;
    line-height: 1;
  }
  .tagline {
    margin-top: 8px;
    font-size: 20px;
    font-weight: 700;
    color: var(--ink-grey);
  }
  .person {
    margin-top: 62px;
    text-align: center;
  }
  .person-name {
    font-size: 34px;
    font-weight: 700;
    color: var(--ink-soft);
    line-height: 1.1;
  }
  .person-title {
    font-size: 17px;
    color: var(--ink-soft);
    margin-top: 4px;
  }
  .contact-list {
    margin-top: 48px;
    display: flex;
    flex-direction: column;
    gap: 10px;
  }
  .contact-row {
    display: flex;
    align-items: center;
    gap: 16px;
    font-size: 24px;
    color: var(--ink-soft);
  }
  .contact-row svg { width: 22px; height: 22px; }
  .address {
    margin-top: 20px;
    text-align: center;
    font-size: 23px;
    color: var(--ink-soft);
    line-height: 1.2;
  }
  .website {
    margin-top: 20px;
    font-size: 23px;
    color: var(--ink-soft);
  }
  .referral-band {
    margin-top: auto;
    width: 100%;
    height: 108px;
    background: linear-gradient(90deg, var(--brand-green-dark), var(--brand-green) 55%, var(--brand-green-light));
    display: flex;
    align-items: center;
    justify-content: center;
    font-size: 32px;
    color: var(--band-text);
  }
</style>
</head>
<body>
  <div class="business-card">
    <div class="brand">
      <div class="brand-mark">
        <span class="brand-dot"></span>
        <span class="brand-name">Pelvora</span>
      </div>
      <div class="tagline">power your home smarter</div>
    </div>

    <div class="person">
      <div class="person-name">Brent Malvaney</div>
      <div class="person-title">Director of Sales and Marketing</div>
    </div>

    <div class="contact-list">
      <div class="contact-row">
        <svg viewBox="0 0 24 24" aria-hidden="true">
          <path fill="var(--brand-green)" d="M3 9c0-3 4-5 9-5s9 2 9 5v2h-5V9H8v2H3z"/>
          <path fill="var(--brand-green)" d="M6 12h12l2 8H4z"/>
          <circle cx="12" cy="16" r="2" fill="#fff"/>
        </svg>
        <span>02 8736 2914</span>
      </div>
      <div class="contact-row">
        <svg viewBox="0 0 24 24" aria-hidden="true">
          <rect x="7" y="2" width="10" height="20" rx="2" fill="var(--brand-green)"/>
          <rect x="9" y="5" width="6" height="9" fill="#fff"/>
        </svg>
        <span>0478 591 830</span>
      </div>
    </div>

    <div class="address">Suite 403, 19 Clover Lane, Sydney<br>NSW 2000</div>
    <div class="website">www.pelvora.com</div>

    <div class="referral-band">referral code: Bmalvaney</div>
  </div>
</body>
</html>
```